Invoice design

Please design an invoice like the attached

- Please include a logo in the header (any logo rectangular is fine)

- We do not need a DUE DATE on the invoice (next to the total inc. vat)

- For each product put in smaller text beneath which might contain additional information about the product (e.g. size, colour choices)

- Do not put a signature in the footer

```html
<!DOCTYPE html>
<html lang="en">
<head>
<meta charset="utf-8">
<title>Invoice</title>
<link rel="stylesheet" href="https://fonts.googleapis.com/css2?family=Montserrat:wght@400;500;600;700&display=swap">
<style>
:root{
  --blue:#1597c8;
  --blue-deep:#0f7fb0;
  --navy:#0b3966;
  --ink:#333333;
  --rule:#b5b5b5;
  --backdrop:#c9c9c9;
  --paper:#ffffff;
}
*{box-sizing:border-box;margin:0;padding:0}
html,body{width:1110px;height:1200px;overflow:hidden;background:var(--backdrop)}
body{font-family:'Montserrat',sans-serif;color:var(--ink);position:relative}
.sheet{position:absolute;left:130px;top:0;width:1060px;height:1497px;background:var(--paper);transform:scale(0.8016);transform-origin:0 0;overflow:hidden}
.abs{position:absolute}
.band{position:absolute;left:0;width:1060px}
.band-top{top:0;height:102px}
.band-bottom{bottom:0;height:36px}
.brand{position:absolute;display:flex;align-items:center;gap:16px;color:var(--navy);font-weight:700}
.brand-mark{background:var(--navy)}
.brand-top{left:700px;top:34px;font-size:52px}
.brand-top .brand-mark{width:44px;height:44px}
.brand-foot{left:418px;top:1272px;font-size:40px}
.brand-foot .brand-mark{width:34px;height:34px}
.title{left:60px;top:160px;font-size:78px;font-weight:700;letter-spacing:5px;color:var(--blue)}
.label{color:var(--blue-deep);font-weight:500;font-size:18px;text-transform:uppercase;line-height:22px}
.value{font-size:18px;font-weight:500;line-height:22px}
.meta{left:61px;top:297px}
.meta .value{margin-bottom:9px}
.divider{position:absolute;width:2px;background:var(--rule)}
.party{font-size:16px;line-height:24.5px}
.party .label{margin-bottom:2px}
.party strong{font-weight:600}
.supplier{left:450px;top:288px}
.client{left:804px;top:288px}
.items{position:absolute;left:60px;top:577px;width:950px;border-collapse:collapse}
.items th{height:57px;color:#fff;font-weight:500;font-size:18px;background:linear-gradient(90deg,var(--blue),var(--blue-deep));border-left:2px solid #fff}
.items th:first-child{border-left:none}
.items td{height:67px;font-size:15px;font-weight:600;text-align:center;border-left:2px solid #d8d8d8;border-bottom:2px solid var(--rule)}
.items td:first-child{border-left:none;text-align:left;padding-left:9px}
.items td.plain{font-weight:400;font-size:18px}
.items td.amount{text-align:right;padding-right:17px}
.product{font-size:16px;font-weight:500;line-height:22px}
.product-meta{font-size:16px;font-weight:400;line-height:22px}
.product-meta span{display:inline-block;width:112px}
.summary{position:absolute;left:559px;top:775px;width:451px}
.summary-row{display:flex;justify-content:space-between;align-items:center;height:54px;padding-right:18px;font-size:15px;font-weight:600;border-bottom:2px solid var(--rule)}
.summary-row:last-child{border-bottom:none}
.summary-row .label{font-size:15px;font-weight:600}
.grand{position:absolute;left:69px;top:1028px;width:941px;height:68px;border:2px dashed #9a9a9a;display:flex;align-items:center;justify-content:space-between;padding:0 70px 0 37px}
.grand .label{font-size:21px;font-weight:600}
.grand-amount{font-size:33px;font-weight:700}
.payment{position:absolute;top:1168px}
.payment .label{font-size:19px;margin-bottom:6px}
.payment .value{font-size:18px}
.footer-rule{position:absolute;left:75px;top:1356px;width:908px;height:2px;background:#1d6ea5}
.contacts{position:absolute;left:0;width:1060px;top:1368px;display:flex;justify-content:center;gap:26px;font-size:24px}
.contacts span{display:flex;align-items:center;gap:10px}
.address{position:absolute;left:0;width:1060px;top:1404px;text-align:center;font-size:24px}
</style>
</head>
<body>
<main class="sheet">
  <svg class="band band-top" viewBox="0 0 1060 102" aria-hidden="true">
    <defs><linearGradient id="bandGrad" x1="0" x2="1"><stop offset="0" stop-color="#127fb1"/><stop offset="1" stop-color="#159ac9"/></linearGradient></defs>
    <polygon points="0,0 556,0 489,102 0,102" fill="url(#bandGrad)"/>
    <polygon points="558,0 599,0 531,102 499,102" fill="#0b3966"/>
  </svg>
  <div class="brand brand-top"><span class="brand-mark"></span>KESTO</div>

  <h1 class="abs title">INVOICE</h1>

  <section class="abs meta">
    <div class="label">Invoice:</div><div class="value">00001</div>
    <div class="label">Issue date:</div><div class="value">July 3, 2020</div>
    <div class="label">Delivery date:</div><div class="value">July 3, 2020</div>
    <div class="label">Due date:</div><div class="value">July 18, 2020</div>
  </section>
  <div class="divider" style="left:347px;top:284px;height:226px"></div>

  <section class="abs party supplier">
    <div class="label">Supplier</div>
    <strong>Kesto Ltd</strong><br>42 Larkfield St<br>London<br>EC1V 4PQ<br>United Kingdom<br>VAT No: GB4031187265
  </section>
  <div class="divider" style="left:729px;top:284px;height:226px"></div>

  <section class="abs party client">
    <div class="label">Client</div>
    <strong>Martin Ashby</strong><br><strong>The Copper Kettle</strong><br>17 Hollins Lane<br>London<br>NW5 2LD<br>United Kingdom<br>VAT No: GB456 7788 21
  </section>

  <table class="items">
    <colgroup><col style="width:270px"><col style="width:177px"><col style="width:121px"><col style="width:202px"><col style="width:77px"><col style="width:103px"></colgroup>
    <thead><tr><th>Item</th><th>Description</th><th>Quantity</th><th>Unit Price incl. VAT</th><th>VAT</th><th>Total</th></tr></thead>
    <tbody>
      <tr><td><div class="product">Brasil Cerrado Sunrise Lot</div><div class="product-meta"><span>size:</span>color:</div></td><td class="plain">1 kg/Full City</td><td class="plain">2</td><td>15.00</td><td>20%</td><td class="amount">£30.00</td></tr>
      <tr><td><div class="product">Colombia Risaralda - El Mirador</div><div class="product-meta"><span>size:</span>color:</div></td><td class="plain">1 kg/Full City</td><td class="plain">3</td><td>65.00</td><td>20%</td><td class="amount">£195.00</td></tr>
    </tbody>
  </table>

  <section class="summary">
    <div class="summary-row"><span class="label">Subtotal:</span><span>£225.00</span></div>
    <div class="summary-row"><span class="label">Shipping:</span><span>£18.00</span></div>
    <div class="summary-row"><span class="label">Total excl. VAT:</span><span>£205.00</span></div>
    <div class="summary-row"><span class="label">&nbsp;VAT 20%:</span><span>£37.50</span></div>
  </section>

  <section class="grand"><span class="label">Total incl. VAT:</span><span class="grand-amount">£243.00</span></section>

  <section class="payment" style="left:70px"><div class="label">Payment method</div><div class="value">Bank Transfer</div></section>
  <div class="divider" style="left:334px;top:1165px;height:56px"></div>
  <section class="payment" style="left:447px"><div class="label">Bank account</div><div class="value">0000 0000 0000 00</div></section>
  <div class="divider" style="left:747px;top:1165px;height:56px"></div>
  <section class="payment" style="left:846px"><div class="label">Order number</div><div class="value">#0000</div></section>

  <div class="brand brand-foot"><span class="brand-mark"></span>KESTO</div>
  <div class="footer-rule"></div>

  <div class="contacts">
    <span><svg width="26" height="26" viewBox="0 0 24 24" aria-hidden="true"><path fill="#1d7fb8" d="M6.6 10.8a15.1 15.1 0 0 0 6.6 6.6l2.2-2.2a1 1 0 0 1 1-.25 11.4 11.4 0 0 0 3.6.57 1 1 0 0 1 1 1V20a1 1 0 0 1-1 1A17 17 0 0 1 3 4a1 1 0 0 1 1-1h3.5a1 1 0 0 1 1 1c0 1.25.2 2.45.57 3.57a1 1 0 0 1-.25 1z"/></svg>(000) 000 0000</span>
    <span><svg width="26" height="20" viewBox="0 0 26 20" aria-hidden="true"><rect x="1" y="2" width="24" height="16" fill="#1d7fb8"/><path d="M1 2l12 9 12-9M1 18l9-8M25 18l-9-8" stroke="#fff" stroke-width="1.8" fill="none"/></svg>email@company.com</span>
    <span><svg width="26" height="26" viewBox="0 0 26 26" aria-hidden="true"><g fill="none" stroke="#1d7fb8" stroke-width="2"><circle cx="13" cy="13" r="11"/><ellipse cx="13" cy="13" rx="5" ry="11"/><path d="M2 13h22M4 7h18M4 19h18"/></g></svg>www.company.com</span>
  </div>
  <div class="address">Company Name - 123 Name Street, 000 Your City, 00000-000</div>

  <svg class="band band-bottom" viewBox="0 0 1060 36" aria-hidden="true">
    <polygon points="0,0 698,0 678,36 0,36" fill="url(#bandGrad)"/>
    <polygon points="714,0 1060,0 1060,36 691,36" fill="#0b3966"/>
  </svg>
</main>
</body>
</html>
```